Business card design needed

Just need something dynamic and unique
For a local painting contractor

Industry/Entity Type

Painting

Contact Information for Business Card

Carl Wexford
Painting Contactor
Interior & Exterior
New Work & Repaints
For an obligation free quote:
0498731046

```html
<!DOCTYPE html>
<html lang="en">
<head>
<meta charset="utf-8">
<title>Carl Wexford – Painting Contactor</title>
<link rel="stylesheet" href="https://fonts.googleapis.com/css2?family=Stardos+Stencil:wght@700&family=Sorts+Mill+Goudy&display=swap">
<style>
  :root {
    --paper: #f7fbfc;
    --paper-edge: #e6f1f4;
    --ink-purple: #4a1e9e;
    --lime: #c9f21b;
    --green: #8eef26;
    --orange: #f7801e;
    --magenta: #ef2fb3;
    --violet: #8a2be2;
  }
  html, body {
    margin: 0;
    padding: 0;
    overflow: hidden;
    background: #ffffff;
  }
  .card {
    position: relative;
    width: 1200px;
    height: 691px;
    overflow: hidden;
    background: radial-gradient(ellipse at 55% 50%, var(--paper) 40%, var(--paper-edge) 100%);
  }
  .splash-art {
    position: absolute;
    inset: 0;
    width: 1200px;
    height: 691px;
  }
  .brand-name {
    position: absolute;
    left: 98px;
    top: 326px;
    margin: 0;
    font-family: "Stardos Stencil", "Courier New", monospace;
    font-weight: 700;
    font-size: 58px;
    line-height: 1;
    letter-spacing: 2px;
    text-transform: uppercase;
    color: var(--ink-purple);
  }
  .trade {
    position: absolute;
    right: 632px;
    top: 390px;
    margin: 0;
    font-family: "Sorts Mill Goudy", Georgia, serif;
    font-size: 31px;
    line-height: 1;
    color: var(--ink-purple);
  }
  .services {
    position: absolute;
    left: 657px;
    top: 593px;
    margin: 0;
    font-family: "Sorts Mill Goudy", Georgia, serif;
    font-size: 27px;
    line-height: 37px;
    color: var(--ink-purple);
  }
</style>
</head>
<body>
<main class="card">
  <svg class="splash-art" viewBox="0 0 1200 691" role="img" aria-label="Bursting multicolour paint splash in lime, orange, red, magenta, violet and blue, trailing into a streaked green brush band" xmlns="http://www.w3.org/2000/svg">
    <defs>
      <radialGradient id="splash-tones" gradientUnits="userSpaceOnUse" cx="260" cy="345" r="440">
        <stop offset="0" stop-color="#d8f51c"/>
        <stop offset="0.5" stop-color="#c9f21b"/>
        <stop offset="0.66" stop-color="#f7a21e"/>
        <stop offset="0.8" stop-color="#ef2fb3"/>
        <stop offset="0.9" stop-color="#8a2be2" stop-opacity="0.55"/>
        <stop offset="1" stop-color="#8a2be2" stop-opacity="0"/>
      </radialGradient>
      <linearGradient id="band-tones" x1="0" y1="0" x2="1" y2="0">
        <stop offset="0" stop-color="#c4f21d"/>
        <stop offset="1" stop-color="#8eef26"/>
      </linearGradient>
    </defs>
    <rect class="brush-band" x="520" y="300" width="680" height="200" fill="url(#band-tones)"/>
    <circle class="splash-burst" cx="260" cy="345" r="440" fill="url(#splash-tones)"/>
  </svg>

  <h1 class="brand-name">Carl Wexford</h1>
  <p class="trade">Painting Contactor</p>
  <p class="services">Interior &amp; Exterior New Work &amp; Repaints<br>For an obligation free quote: 0498731046</p>
</main>
</body>
</html>
```